Vitalquorra.com

I need a web design for a Online Wellness Center based in Chicago, IL and it's called "Vitalquorra" We provide Health risk assessment to individuals and interventions. Our portal has a Health Activity tracker where our members record health activities and aerobic miles and biometric data. Our Online wellness center tracks the participant's progress toward health goals and awards points for completed activities.
I started working on this website but the designer was not able to designer a website which describes what we do. I need a fresh look on this project. I need a very attractive, responsive website which says what we do.
These are the things we do.
1. We provide Health Risk Assessments to individuals and Co-operations
2. We Provide Free health screenings to undeserved communities
3. Assist individuals access free or affordable medications
4. We ask providers/doctors to see (or do a complete physical) one individual free of charge once a year (those individuals who are no insured and don't have money to pay from their pocket)
5. Assist patient access lab work at low cost
Our goal is to provide services that will lower the cost of care for our members.

Here is the website: www.vitalquorra.com still underdevelopment. PLEASE DO NOT COPY THIS STYLE OF WEBSITE. IT'S A BAD DESIGN AND THAT IS WHY I'M RE-DESIGNING THE SITE

Target Market(s)

Health individuals between the age of 21 to 65 Plus years old. Insured and uninsured

Industry/Entity Type

Health And Wellness

Coding

Coded - Design and coding required

Number of Pages Required

5+ page

Colors
0292cd

Requirements
Must have
• I'm still working on this websiteHere is the menu: Home, About us, Services, Health Screening, Providers, Contacts
• Please see. www.vitalquorra.com
Nice to have
• Event calender
• Upcoming Event
• Medication
• Lab assist
• Providers/Free Clinics

```html
<!DOCTYPE html>
<html lang="en">
<head>
<meta charset="utf-8">
<title>Vitalquorra – Online Wellness Center</title>
<link rel="stylesheet" href="https://fonts.googleapis.com/css2?family=Oswald:wght@400;500&family=Open+Sans:wght@400;600;700&display=swap">
<style>
:root{
  --blue:#0292cd;
  --blue-dark:#0277a8;
  --ink:#2f3337;
  --text:#6b6f73;
  --night:#1e2329;
  --night-2:#2b3037;
  --night-3:#353b42;
  --mist:#f1f3f4;
  --sky:#e6f1f8;
  --white:#ffffff;
}
*{box-sizing:border-box;margin:0;padding:0}
html,body{width:1200px;height:2308px;overflow:hidden}
body{font-family:"Open Sans",Arial,sans-serif;color:var(--text);background:var(--white);position:relative;font-size:13px;line-height:1.6}
.wrap{width:1000px;margin:0 auto;position:relative}
.btn{display:inline-block;background:var(--blue);color:var(--white);font-size:11px;font-weight:700;letter-spacing:.5px;padding:8px 16px;text-transform:uppercase}
.btn-text{color:var(--white);font-size:11px;font-weight:700;text-transform:uppercase}

/* header */
.site-header{position:absolute;top:0;left:0;width:1200px;height:64px;background:var(--night)}
.site-header .wrap{height:64px;display:flex;align-items:center;justify-content:space-between}
.brand{display:flex;align-items:center;gap:10px;color:var(--white);font-family:"Open Sans",sans-serif;font-weight:700;font-size:26px}
.brand-dot{width:22px;height:22px;border-radius:50%;background:var(--blue)}
.phone{display:flex;align-items:center;gap:8px;color:var(--white);font-size:22px;font-weight:600}
.main-nav{position:absolute;top:64px;left:0;width:1200px;height:44px;background:var(--night-2)}
.main-nav ul{list-style:none;display:flex;width:1000px;margin:0 auto;height:44px}
.main-nav li{flex:1;text-align:center;line-height:44px;color:var(--white);font-size:12px;font-weight:600;text-transform:uppercase;border-right:1px solid #40464e}
.main-nav li:first-child{border-left:1px solid #40464e}
.main-nav li.active{background:var(--blue)}

/* hero */
.hero{position:absolute;top:108px;left:0;width:1200px;height:372px;background:linear-gradient(90deg,#c9dfee 0%,#e9f2f8 45%,#f4f8fb 100%)}
.hero-photo{position:absolute;left:100px;top:0;width:520px;height:372px;background:linear-gradient(135deg,#a9c7dc,#dde9f1 60%,#eef4f8)}
.hero-title{position:absolute;left:560px;top:140px;width:560px;font-family:"Oswald",sans-serif;font-weight:400;font-size:30px;line-height:1.35;color:var(--ink);text-transform:uppercase}

/* welcome */
.welcome{position:absolute;top:480px;left:0;width:1200px;height:380px}
.welcome-intro{position:absolute;left:100px;top:50px;width:260px}
.welcome-intro .kicker{font-size:15px;color:var(--ink);font-weight:600}
.welcome-intro h2{font-family:"Open Sans",sans-serif;font-weight:700;color:var(--blue);font-size:34px;line-height:1.1}
.welcome-intro .tag{font-size:11px;color:var(--blue);font-weight:600;margin:4px 0 12px}
.welcome-intro p{font-size:11.5px;margin-bottom:16px}
.welcome-curve{position:absolute;left:370px;top:30px}
.services{position:absolute;left:460px;top:40px;width:640px;display:grid;grid-template-columns:1fr 1fr;gap:24px 30px}
.service{display:flex;align-items:center;gap:14px;font-size:13px;color:var(--ink)}
.service.wide{grid-column:1 / 3}
.icon-ring{flex:none;width:56px;height:56px;border:2px solid var(--blue);border-radius:50%;display:flex;align-items:center;justify-content:center}

/* medication */
.medication{position:absolute;top:860px;left:0;width:1200px;height:340px;background:var(--mist)}
.medication-photo{position:absolute;left:0;top:0;width:600px;height:340px;background:radial-gradient(ellipse at 55% 55%,#e9c3a3 0%,#d9a887 30%,#f1ede8 70%)}
.medication-body{position:absolute;left:612px;top:40px;width:488px}
.section-title{font-family:"Oswald",sans-serif;font-weight:400;font-size:36px;color:var(--blue);line-height:1.2;margin-bottom:12px}
.medication-body p{font-size:11.5px;margin-bottom:12px}

/* program cards */
.programs{position:absolute;top:1224px;left:100px;width:1000px;height:290px;display:flex;gap:20px}
.program{flex:1;position:relative;padding:22px 26px;color:#d8dcdf}
.program.lab{background:var(--night-3)}
.program.clinic{background:var(--blue);color:#e3f3fb}
.program h3{font-family:"Oswald",sans-serif;font-weight:400;font-size:36px;color:var(--white);line-height:1.2}
.program p{width:270px;font-size:11px;margin-top:60px}
.program .icon-box{position:absolute;right:30px;top:26px;width:150px;height:150px;display:flex;align-items:center;justify-content:center}
.program.lab .icon-box{background:#4a5058}
.program.clinic .icon-box{background:#2aa6da}
.program .btn-text{position:absolute;right:30px;bottom:24px}

/* events */
.events{position:absolute;top:1540px;left:0;width:1200px;height:340px;background:var(--sky)}
.events-head{position:absolute;left:100px;top:22px;width:580px;display:flex;justify-content:space-between;align-items:center}
.events-head h2{font-family:"Oswald",sans-serif;font-weight:400;font-size:38px;color:var(--ink)}
.arrows{display:flex;gap:6px}
.arrows span{width:22px;height:22px;border-radius:50%;border:1px solid #9aa4ab;display:flex;align-items:center;justify-content:center}
.event-list{position:absolute;left:100px;top:90px;width:580px;display:flex;gap:20px}
.event{flex:1}
.event-photo{height:120px;background:linear-gradient(135deg,#cfe3ef,#f4f8fa)}
.event h4{color:var(--blue);font-size:14px;font-weight:700;margin-top:8px}
.event .date{font-size:11px;color:var(--ink)}
.event p{font-size:11px}
.calendar{position:absolute;left:720px;top:18px;width:380px;background:var(--white)}
.cal-head{background:var(--blue);height:44px;display:flex;align-items:center;justify-content:space-between;padding:0 12px}
.cal-head .month{background:var(--white);color:var(--blue);font-family:"Oswald",sans-serif;font-size:20px;padding:0 26px;line-height:32px}
.cal-head .nav{width:22px;height:22px;background:rgba(255,255,255,.25);display:flex;align-items:center;justify-content:center}
.calendar table{width:100%;border-collapse:collapse;font-size:11px;color:var(--ink)}
.calendar th{background:#e9eef1;font-weight:600;height:28px}
.calendar td{border:1px solid #e1e6e9;height:40px;text-align:left;vertical-align:top;padding:3px 5px}
.calendar td.off{color:#b7bdc1}
.calendar td.today{background:var(--blue);color:var(--white)}
.calendar td.mark{background:#dcecf6}

/* newsletter */
.newsletter{position:absolute;top:1880px;left:0;width:1200px;height:84px;background:var(--night-2)}
.newsletter .wrap{display:flex;align-items:center;height:84px;gap:18px}
.newsletter .copy{width:290px}
.newsletter .copy strong{display:block;color:var(--blue);font-family:"Oswald",sans-serif;font-weight:400;font-size:20px;line-height:1.1}
.newsletter .copy span{color:#c3c8cc;font-size:12px}
.field{display:flex;align-items:center;gap:10px;color:#c3c8cc;font-size:12px}
.field i{display:block;width:200px;height:30px;background:var(--white)}
.newsletter .btn{padding:9px 26px}

/* footer */
.site-footer{position:absolute;top:1964px;left:0;width:1200px;height:310px;background:var(--night)}
.footer-cols{display:flex;padding-top:32px;gap:40px}
.footer-col h5{font-family:"Oswald",sans-serif;font-weight:400;color:var(--blue);font-size:20px;margin-bottom:16px}
.footer-col{color:#b9bfc4;font-size:12px}
.footer-col.links{width:330px}
.footer-col.contact{width:320px}
.link-grid{display:grid;grid-template-columns:1fr 1fr;gap:6px 20px;list-style:none}
.link-grid li::before{content:"› ";color:var(--blue)}
.contact-row{display:flex;gap:10px;margin-bottom:10px;align-items:flex-start}
.social{display:grid;grid-template-columns:1fr 1fr;gap:14px 20px}
.social div{display:flex;align-items:center;gap:10px}
.social b{width:26px;height:26px;border-radius:50%;background:var(--night-3);display:block}
.legal{position:absolute;top:2274px;left:0;width:1200px;height:34px;background:#15191d;color:#8e959b;font-size:11px;text-align:center;line-height:34px}
</style>
</head>
<body>

<header class="site-header">
  <div class="wrap">
    <div class="brand"><span class="brand-dot"></span>Vitalquorra</div>
    <div class="phone">
      <svg width="20" height="20" viewBox="0 0 24 24"><path fill="#0292cd" d="M6.6 10.8a15 15 0 0 0 6.6 6.6l2.2-2.2a1 1 0 0 1 1-.25 11.4 11.4 0 0 0 3.6.57 1 1 0 0 1 1 1V20a1 1 0 0 1-1 1A17 17 0 0 1 3 4a1 1 0 0 1 1-1h3.5a1 1 0 0 1 1 1c0 1.25.2 2.45.57 3.57a1 1 0 0 1-.25 1z"/></svg>
      +123 456 780
    </div>
  </div>
</header>
<nav class="main-nav">
  <ul>
    <li class="active">Home</li><li>About us</li><li>Services</li><li>Health Screening</li><li>Providers</li><li>Contacts</li>
  </ul>
</nav>

<section class="hero">
  <div class="hero-photo" role="img" aria-label="Doctor in a white coat holding a medical chart"></div>
  <h1 class="hero-title">We are non profit organization whose main aim is only to make healthy USA.</h1>
</section>

<section class="welcome">
  <div class="welcome-intro">
    <div class="kicker">Welcome to</div>
    <h2>Vitalquorra</h2>
    <div class="tag">The online wellness center</div>
    <p>We help members track health activities, aerobic miles and biometric data, and we award points for every completed goal. Our programs aim to lower the cost of care for insured and uninsured people across the country.</p>
    <span class="btn">Read more</span>
  </div>
  <svg class="welcome-curve" width="80" height="320" viewBox="0 0 80 320">
    <path d="M10 10 C70 60 70 260 10 310" fill="none" stroke="#0292cd" stroke-width="3"/>
    <circle cx="10" cy="10" r="6" fill="#0292cd"/><circle cx="10" cy="310" r="6" fill="#0292cd"/>
  </svg>
  <div class="services">
    <div class="service"><span class="icon-ring"><svg width="26" height="26" viewBox="0 0 24 24"><path d="M5 3h14v18H5z" fill="none" stroke="#0292cd" stroke-width="2"/><path d="M8 8h8M8 12h8M8 16h5" stroke="#0292cd" stroke-width="2"/></svg></span>Health Risk Assessments to individuals and Co-operations</div>
    <div class="service"><span class="icon-ring"><svg width="26" height="26" viewBox="0 0 24 24"><path d="M12 21s-8-5-8-11a4 4 0 0 1 8-1 4 4 0 0 1 8 1c0 6-8 11-8 11z" fill="none" stroke="#0292cd" stroke-width="2"/></svg></span>Free health screenings to underserved communities</div>
    <div class="service"><span class="icon-ring"><svg width="26" height="26" viewBox="0 0 24 24"><rect x="4" y="9" width="16" height="7" rx="3.5" fill="none" stroke="#0292cd" stroke-width="2"/><path d="M12 9v7" stroke="#0292cd" stroke-width="2"/></svg></span>Assist individuals access free or affordable medications</div>
    <div class="service"><span class="icon-ring"><svg width="26" height="26" viewBox="0 0 24 24"><path d="M9 3h6M10 3v6l-5 10h14l-5-10V3" fill="none" stroke="#0292cd" stroke-width="2"/></svg></span>Assist patient access lab work at low cost</div>
    <div class="service wide"><span class="icon-ring"><svg width="26" height="26" viewBox="0 0 24 24"><circle cx="12" cy="8" r="4" fill="none" stroke="#0292cd" stroke-width="2"/><path d="M4 21c0-4 4-7 8-7s8 3 8 7" fill="none" stroke="#0292cd" stroke-width="2"/></svg></span>We ask providers/doctors to see (or do a complete physical) one individual free of charge once a year (those individuals who are not insured and don't have money to pay from their pocket)</div>
  </div>
</section>

<section class="medication">
  <div class="medication-photo" role="img" aria-label="Open hands holding colourful pills and capsules"></div>
  <div class="medication-body">
    <h2 class="section-title">Medication</h2>
    <p>We connect members with programs that provide free or affordable prescriptions. Our team reviews your needs, finds matching assistance options and helps you complete every form so medicine reaches you without delay.</p>
    <p>Members can track refills and doses in the online portal, earn points for sticking to their plans and share progress with their providers.</p>
    <span class="btn">Read more</span>
  </div>
</section>

<section class="programs">
  <article class="program lab">
    <h3>Lab assist</h3>
    <p>Get blood work and routine lab tests at a low cost through our partner labs near your home.</p>
    <div class="icon-box" role="img" aria-label="Illustration of a doctor"></div>
    <span class="btn-text">Read more</span>
  </article>
  <article class="program clinic">
    <h3>Free Clinics</h3>
    <p>Find providers who see one uninsured patient free of charge each year for a complete physical.</p>
    <div class="icon-box"><svg width="90" height="90" viewBox="0 0 24 24"><path d="M3 10l9-6 9 6v11H3z" fill="none" stroke="#fff" stroke-width="1.4"/><path d="M12 10v7M8.5 13.5h7" stroke="#fff" stroke-width="1.8"/></svg></div>
    <span class="btn-text">Read more</span>
  </article>
</section>

<section class="events">
  <div class="events-head">
    <h2>Upcoming Event</h2>
    <div class="arrows">
      <span><svg width="8" height="10" viewBox="0 0 8 10"><path d="M6 1L2 5l4 4" fill="none" stroke="#6b6f73" stroke-width="1.5"/></svg></span>
      <span><svg width="8" height="10" viewBox="0 0 8 10"><path d="M2 1l4 4-4 4" fill="none" stroke="#6b6f73" stroke-width="1.5"/></svg></span>
    </div>
  </div>
  <div class="event-list">
    <article class="event">
      <div class="event-photo" role="img" aria-label="Group of medical staff in white coats"></div>
      <h4>Free screening day</h4>
      <div class="date">September 14, 2015</div>
      <p>Blood pressure, glucose and cholesterol checks open to everyone in the community.</p>
    </article>
    <article class="event">
      <div class="event-photo" role="img" aria-label="Doctor consulting with a patient"></div>
      <h4>Wellness walk</h4>
      <div class="date">September 22, 2015</div>
      <p>Log your aerobic miles with friends and earn bonus points for each lap.</p>
    </article>
  </div>
  <div class="calendar">
    <div class="cal-head">
      <span class="nav"><svg width="8" height="10" viewBox="0 0 8 10"><path d="M6 1L2 5l4 4" fill="none" stroke="#fff" stroke-width="1.5"/></svg></span>
      <span class="month">September 2015</span>
      <span class="nav"><svg width="8" height="10" viewBox="0 0 8 10"><path d="M2 1l4 4-4 4" fill="none" stroke="#fff" stroke-width="1.5"/></svg></span>
    </div>
    <table>
      <tr><th>MO</th><th>TU</th><th>WE</th><th>TH</th><th>FR</th><th>SA</th><th>SU</th></tr>
      <tr><td class="off">31</td><td>1</td><td>2</td><td>3</td><td>4</td><td>5</td><td>6</td></tr>
      <tr><td>7</td><td>8</td><td>9</td><td>10</td><td>11</td><td>12</td><td>13</td></tr>
      <tr><td class="today">14</td><td>15</td><td>16</td><td>17</td><td>18</td><td>19</td><td>20</td></tr>
      <tr><td>21</td><td class="mark">22</td><td>23</td><td>24</td><td>25</td><td>26</td><td>27</td></tr>
      <tr><td>28</td><td>29</td><td>30</td><td class="off">1</td><td class="off">2</td><td class="off">3</td><td class="off">4</td></tr>
    </table>
  </div>
</section>

<section class="newsletter">
  <div class="wrap">
    <div class="copy"><strong>Want to stay in touch?</strong><span>Sign up for a newsletter</span></div>
    <label class="field">Name <i></i></label>
    <label class="field">Email <i></i></label>
    <span class="btn">Sign up</span>
  </div>
</section>

<footer class="site-footer">
  <div class="wrap footer-cols">
    <div class="footer-col links">
      <h5>Quick Links</h5>
      <ul class="link-grid">
        <li>Home</li><li>Providers</li>
        <li>About us</li><li>Contact us</li>
        <li>Services</li><li>Upcoming Events</li>
        <li>Health Screening</li>
      </ul>
    </div>
    <div class="footer-col contact">
      <h5>Contact Us</h5>
      <div class="contact-row"><svg width="14" height="16" viewBox="0 0 24 24"><path d="M12 2a7 7 0 0 0-7 7c0 5 7 13 7 13s7-8 7-13a7 7 0 0 0-7-7zm0 9.5A2.5 2.5 0 1 1 12 6.5a2.5 2.5 0 0 1 0 5z" fill="#0292cd"/></svg><span>240 Lake Street Suite 12<br>Chicago, IL 60601</span></div>
      <div class="contact-row"><svg width="14" height="14" viewBox="0 0 24 24"><path fill="#0292cd" d="M6.6 10.8a15 15 0 0 0 6.6 6.6l2.2-2.2a1 1 0 0 1 1-.25 11.4 11.4 0 0 0 3.6.57 1 1 0 0 1 1 1V20a1 1 0 0 1-1 1A17 17 0 0 1 3 4a1 1 0 0 1 1-1h3.5a1 1 0 0 1 1 1c0 1.25.2 2.45.57 3.57a1 1 0 0 1-.25 1z"/></svg><span>+123 456 780</span></div>
      <div class="contact-row"><svg width="14" height="14" viewBox="0 0 24 24"><path d="M3 5h18v14H3z" fill="none" stroke="#0292cd" stroke-width="2"/><path d="M3 5l9 8 9-8" fill="none" stroke="#0292cd" stroke-width="2"/></svg><span>hello@vitalquorra.com</span></div>
    </div>
    <div class="footer-col">
      <h5>Connect Us</h5>
      <div class="social">
        <div><b></b>Newsfeed</div><div><b></b>Shortposts</div>
        <div><b></b>Newsfeed</div><div><b></b>Shortposts</div>
      </div>
    </div>
  </div>
</footer>
<div class="legal">Vitalquorra © 2015 | All Rights Reserved</div>

</body>
</html>
```